Corvell Tarn manufacturing Project

We are looking at getting a brand new design for a new company that deals in selling stainless tubing and other stainless still products such as handrails, Spigots, Balustrade Fittings
Glass, Glass fittings and Aluminium Channels

We require a very clean website that deals with the following colours:

Blue to light blues
Blacks
Greys to light Greys
Whites

We are open for other ideas BUT we *DO NOT* want any pinks, greens or bright colours except for backgrounds colours we have chosen above. (It can be solid, gradient or a subtle pattern)

YOU MUST KEEP THE LOGO AS IS. PLEASE DO NOT ALTER THE LOGO IN *ANY WAY* and the logo MUST be the same colours and fonts.

Logo is attached.

The site must contain these aspects:
jQuery Slider (Image slide show)
Top drop down Menus
Be no more than 900px wide
Text is to be to the k9R standards. (no special fonts)

We will chop up the design into html format. You just need to provide the PSD file.

The clients opposition is:
www.polbrenwick.com

It Company

• Alter the logo in anyway

```html
<!DOCTYPE html>
<html lang="en">
<head>
<meta charset="utf-8">
<title>Corvell Tarn – Stainless Products</title>
<link href="https://fonts.googleapis.com/css2?family=Roboto:wght@300;400;500;700&family=Roboto+Slab:wght@400;700&display=swap" rel="stylesheet">
<style>
:root{
  --page:#f7f7f6;
  --ink:#222;
  --muted:#666;
  --blue:#1f5a96;
  --blue-dark:#13467a;
  --blue-hero:#4a8cc6;
  --blue-hero-light:#9cc3e6;
  --nav-top:#8a8a8a;
  --nav-bot:#4e4e4e;
  --line:#dcdcdc;
  --white:#fff;
  --footer:#efefef;
}
*{margin:0;padding:0;box-sizing:border-box}
html,body{width:910px;height:1200px;overflow:hidden}
body{background:var(--page);font-family:"Roboto",Arial,sans-serif;color:var(--ink);position:relative}
.abs{position:absolute}

.brand{left:40px;top:12px;width:150px;text-align:center}
.brand-mark{width:90px;height:90px;border-radius:50%;background:#1c1c1c;margin:0 auto}
.brand-name{font-family:"Roboto Slab",Georgia,serif;font-size:16px;color:#222;margin-top:6px;line-height:1.1}
.brand-sub{font-family:"Roboto Slab",Georgia,serif;font-size:9px;color:#222;letter-spacing:.3px}

.top-photo{left:715px;top:0;width:195px;height:42px;background:linear-gradient(90deg,#f2f2f2,#c8c8c8,#eee)}

.social{top:66px;left:331px;display:flex;gap:8px}
.social span{font-size:12px;font-weight:700;color:var(--blue);padding:3px 4px}

.search{left:524px;top:60px;width:195px;height:28px;border:1px solid #ccc;background:#fff;display:flex;align-items:center}
.search span{font-size:12px;color:#999;padding-left:26px;flex:1}
.search svg.mag{position:absolute;left:8px;top:7px}
.search .go{width:32px;height:28px;background:#555;display:flex;align-items:center;justify-content:center;margin-right:-1px}
.help{left:731px;top:57px}
.help small{display:block;font-size:11px;color:#777}
.help strong{display:block;font-size:17px;color:var(--blue);font-weight:700}

.nav{left:252px;top:101px;width:611px;height:34px;background:linear-gradient(var(--nav-top),var(--nav-bot));display:flex;border-radius:2px;overflow:hidden}
.nav a{color:#fff;font-size:12.5px;font-weight:700;text-decoration:none;height:34px;line-height:34px;text-align:center;white-space:nowrap;flex:none}
.nav a.active{background:#fff;color:var(--blue)}
.dropdown{left:386px;top:135px;width:211px;height:193px;background:#fff;box-shadow:0 3px 8px rgba(0,0,0,.25);padding-top:12px;z-index:3}
.dropdown li{list-style:none;font-size:12px;color:#444;height:23.4px;line-height:23.4px;padding-left:22px;margin:0 9px}
.dropdown li.on{background:var(--blue);color:#fff;padding-left:13px}

.hero{left:0;top:156px;width:910px;height:389px;background:linear-gradient(100deg,var(--blue-hero) 0%,#6aa3d4 50%,var(--blue-hero-light) 75%,#d8e8f4 100%)}
.hero-title{left:46px;top:258px;color:#fff;font-size:37px;font-weight:300;line-height:38px}
.hero-title b{font-weight:700}
.hero-text{left:46px;top:340px;width:430px;color:#eaf2fa;font-size:15px;line-height:20px;font-weight:300}
.hero-btn{left:46px;top:421px;width:222px;height:33px;background:#fff;color:var(--blue-dark);font-family:"Roboto Slab",serif;font-weight:700;font-size:14px;display:flex;align-items:center;justify-content:center;gap:8px;letter-spacing:.4px}

.h2{font-size:16px;font-weight:700;color:#111}
.feature{top:589px;width:297px;height:179px;background:linear-gradient(90deg,#7e8b92,#a6b0b5)}
.feature .ph{position:absolute;right:0;top:0;width:148px;height:179px;background:linear-gradient(90deg,rgba(255,255,255,0),rgba(235,238,240,.55))}
.feature h3{position:absolute;left:23px;top:25px;color:#fff;font-size:19px;font-weight:700}
.feature h4{position:absolute;left:23px;top:51px;color:#fff;font-size:14px;font-weight:400}
.feature p{position:absolute;left:23px;top:72px;width:130px;color:#e4e8ea;font-size:12px;line-height:14.5px}
.feature .btn{position:absolute;left:23px;top:125px;width:122px;height:26px;background:var(--blue);color:#fff;font-family:"Roboto Slab",serif;font-size:11px;font-weight:700;display:flex;align-items:center;justify-content:center;letter-spacing:.5px}

.side{left:666px;width:197px;background:#fff;border:1px solid var(--line)}
.side-help{top:588px;height:123px}
.side-help .ph{position:absolute;left:0;top:0;width:82px;height:121px;background:linear-gradient(#e8e8e8,#cfcfcf)}
.side-help b{position:absolute;right:10px;top:34px;font-size:19px;color:var(--blue);font-weight:700}
.side-help small{position:absolute;right:8px;top:59px;font-size:9.5px;color:#777}
.side-help em{position:absolute;right:8px;top:78px;font-family:"Roboto Slab",serif;font-style:normal;font-size:16px;color:#777}
.side-help .online{position:absolute;right:0;bottom:0;width:75px;height:17px;background:var(--blue);color:#fff;font-size:12px;font-weight:700;text-align:center;line-height:17px}
.side-cat{top:724px;height:216px}
.side-cat .txt{position:absolute;right:12px;top:20px;text-align:right;font-size:19px;color:#555;font-weight:300;line-height:21px}
.side-cat .txt b{color:var(--blue);font-weight:700}
.side-cat .ph{position:absolute;left:6px;top:100px;width:182px;height:110px;background:linear-gradient(160deg,#dfe3e6,#b4bcc2)}

.tile{top:805px;width:195px;height:136px;background:#fff;border:1px solid var(--line)}
.tile .ph{position:absolute;left:35px;top:8px;width:125px;height:95px;background:radial-gradient(circle,#d0d3d5,#fff 70%)}
.tile span{position:absolute;left:15px;bottom:6px;font-size:13px;font-weight:700;color:var(--blue)}

.footer{left:0;top:984px;width:910px;height:216px;background:var(--footer);border-top:1px solid #e2e2e2}
.f-brand{left:52px;top:1030px;width:58px;text-align:center}
.f-brand .brand-mark{width:42px;height:42px;background:#888}
.f-brand .brand-name{font-size:8px;color:#777}
.f-col h5{font-size:13px;font-weight:400;color:var(--blue);margin-bottom:8px}
.f-col p{font-size:11.5px;color:#777;line-height:17px}
.f-about{left:133px;top:1023px;width:262px}
.f-contact{left:436px;top:1023px;width:150px}
.f-contact .row{display:flex;align-items:center;gap:8px;font-size:11px;font-weight:700;color:#555;margin-top:6px;white-space:nowrap}
.f-map{left:624px;top:1023px;width:250px}
.f-map .links{font-size:11.5px;color:#888;line-height:19px}
.f-map .links b{color:var(--blue)}
.f-map .copy{font-size:10.5px;color:#888;margin-top:8px}
.divider{top:1020px;width:1px;height:140px;background:#dcdcdc}
</style>
</head>
<body>

<div class="abs brand">
  <div class="brand-mark"></div>
  <div class="brand-name">Corvell Tarn</div>
  <div class="brand-sub">Manufacturing Co. Ltd</div>
</div>

<div class="abs top-photo" role="img" aria-label="Polished stainless spigot fittings"></div>

<div class="abs social"><span>Chatterly</span><span>Friendnet</span><span>Clipcast</span></div>

<div class="abs search">
  <svg class="mag" width="13" height="13" viewBox="0 0 13 13"><circle cx="5.5" cy="5.5" r="4" fill="none" stroke="#999" stroke-width="1.5"/><line x1="8.5" y1="8.5" x2="12" y2="12" stroke="#999" stroke-width="1.5"/></svg>
  <span>Search</span>
  <div class="go"><svg width="10" height="12" viewBox="0 0 10 12"><path d="M2 1l6 5-6 5" fill="none" stroke="#fff" stroke-width="2.2"/></svg></div>
</div>
<div class="abs help"><small>How May We Help?</small><strong>Call 800-555-0142</strong></div>

<nav class="abs nav">
  <a href="#" style="width:84px">HOME</a><a href="#" style="width:50px">ABOUT</a><a href="#" class="active" style="width:96px">PRODUCTS</a><a href="#" style="width:95px">DOWNLOAD</a><a href="#" style="width:94px">PRODUCTS</a><a href="#" style="width:97px">DOWNLOAD</a><a href="#" style="width:95px">CONTACT</a>
</nav>

<div class="abs hero" role="img" aria-label="Stainless steel tubes against a blue glass building with wind turbines"></div>
<h1 class="abs hero-title">The <b>Leading Manufacturer</b><br>in <b>Stainless</b> Products</h1>
<p class="abs hero-text">Innovative's glass component aluminum railing system are strong, aesthetically pleasing, and maintenance free. The transparent glass allows for a less obstructed view.</p>
<div class="abs hero-btn">LEARN MORE ABOUT US <svg width="8" height="12" viewBox="0 0 8 12"><path d="M1.5 1l5 5-5 5" fill="none" stroke="#13467a" stroke-width="2.4"/></svg></div>

<ul class="abs dropdown">
  <li>RailingSystem(42.4,33.7,48.3)</li>
  <li>RailingSystem(2″,1.5″,43)</li>
  <li class="on">Glass System</li>
  <li>Post &amp; Balustrade</li>
  <li>Accessories</li>
  <li>Square tube Fittings</li>
  <li>Sliding door &amp; Canopy</li>
</ul>

<h2 class="abs h2" style="left:46px;top:566px">Featured Products</h2>
<div class="abs feature" style="left:46px">
  <div class="ph" role="img" aria-label="Aluminium glass channel profile"></div>
  <h3>Railing System</h3><h4>(42.4,33.7,48.3)</h4>
  <p>Custom twisted in wire brushes, gun brushes, medical brushes,</p>
  <div class="btn">VIEW PRODUCTS</div>
</div>
<div class="abs feature" style="left:352px">
  <div class="ph" role="img" aria-label="Aluminium glass channel profile"></div>
  <h3>Railing System</h3><h4>(42.4,33.7,48.3)</h4>
  <p>Custom twisted in wire brushes, gun brushes, medical brushes,</p>
  <div class="btn">VIEW PRODUCTS</div>
</div>

<div class="abs side side-help">
  <div class="ph" role="img" aria-label="Support agent wearing a headset"></div>
  <b>Need Help!</b><small>CHAT ONLINE WITH US</small><em>Live Support</em>
  <div class="online">ONLINE</div>
</div>
<div class="abs side side-cat">
  <div class="txt">Download<br>Your Digital<br><b>Catalogue</b><br>Here!</div>
  <div class="ph" role="img" aria-label="Open product catalogue"></div>
</div>

<h2 class="abs h2" style="left:46px;top:783px">All Products</h2>
<div class="abs tile" style="left:46px"><div class="ph" role="img" aria-label="Stainless elbow fitting"></div><span>Bent, Pin&amp;Plate</span></div>
<div class="abs tile" style="left:250px"><div class="ph" role="img" aria-label="Stainless glass clamp"></div><span>Glass Clamp 50.8mm</span></div>
<div class="abs tile" style="left:454px"><div class="ph" role="img" aria-label="Stainless glass holder"></div><span>Glass Holder</span></div>

<footer class="abs footer"></footer>
<div class="abs f-brand"><div class="brand-mark"></div><div class="brand-name">Corvell Tarn</div></div>
<div class="abs f-col f-about">
  <h5>ABOUT CORVELL TARN</h5>
  <p>Welcome to corvell tarn, your partner for professional railing, glass securing and glass channel systems. Find out more about new products and new ideas, our product range, quality and safety, functionality and design along side our philosophy, our company and the idea behind it.</p>
</div>
<div class="abs divider" style="left:410px"></div>
<div class="abs f-col f-contact">
  <h5>CONTACT US</h5>
  <p>Corvell Tarn, Unit 12 - Harrow Point, Brenley Road, Ashdale, AS4 9QX</p>
  <div class="row" style="margin-top:12px"><svg width="9" height="12" viewBox="0 0 9 12"><rect x="0.5" y="0.5" width="8" height="11" rx="1.5" fill="#666"/><rect x="2" y="2" width="5" height="6" fill="#eee"/></svg>+44 - 0800-5550198</div>
  <div class="row"><svg width="11" height="8" viewBox="0 0 11 8"><rect width="11" height="8" fill="#666"/><path d="M0 0l5.5 4.5L11 0" fill="none" stroke="#eee" stroke-width="1"/></svg>support@corvelltarn.com</div>
</div>
<div class="abs divider" style="left:598px"></div>
<div class="abs f-col f-map">
  <h5>SITEMAP</h5>
  <div class="links"><b>Home</b> · About · Products · Download · Contact<br>Services · Team · Download · Contact</div>
  <div class="copy">© 2008 Corvell Tarn. All Rights Reserved</div>
</div>

</body>
</html>
```